Keldro Cybersecurity Secives professional web site

Keldro is a unit of the Vostemic company, based on the audit services it offers and which mainly works by the contacts it has from its previous experience. The objective with the development of this website will be to increase its presence on the internet and even link the traffic of its social networks with the blog of the new page and in this way, provide information for old and potential customers.
For this reason, we will set the objective of the page, have all the information of the company, its services and its scope in general, in a formal and simple for users, facilitating the task of finding the information they want within of the page, as well as, including the option of feedback.
Updates

Need extra days to review

Target Market(s)

any company that needs security assessments

Number of Pages Required

4 page

Font styles to use
Sans Serif

Colors

Designer to choose colors to be used in the design.

Requirements
Must have
• READ THE PDF PLEASE. Video in homepage, cool graphics, color like our logo
• I like the following sites: www.vostemic-example.com & www.gantrelo-example.com
Nice to have
• Futuristic
Should not have
• Please, dont use the gallery pictures I used in my document, I prefer hand made illustrations instead

```html
<!DOCTYPE html>
<html lang="en">
<head>
<meta charset="utf-8">
<title>Keldro Security</title>
<link rel="stylesheet" href="https://fonts.googleapis.com/css2?family=Roboto:wght@400;500;700&family=Arimo:wght@400&display=swap">
<style>
:root{
  --navy:#03097a;
  --ink:#0d1b3d;
  --red:#c8101e;
  --grey:#8a8a8a;
  --text:#666;
  --line:#d9d9d9;
  --white:#fff;
}
*{box-sizing:border-box;margin:0;padding:0}
html,body{width:1200px;height:604px;overflow:hidden;background:var(--white)}
body{position:relative;font-family:'Roboto',sans-serif}
.site-header{position:absolute;left:0;top:0;width:1200px;height:82px;background:var(--white);box-shadow:0 2px 5px rgba(0,0,0,.08)}
.brand{position:absolute;left:61px;top:28px}
.brand-name{font-family:'Roboto',sans-serif;font-weight:500;font-size:24px;line-height:26px;color:var(--ink);letter-spacing:.5px}
.lang{position:absolute;top:11px;left:942px;display:flex;align-items:center;gap:8px}
.lang-label{font-size:9px;color:var(--grey);letter-spacing:.4px}
.lang-select{width:132px;height:23px;border:1px solid var(--navy);display:flex;align-items:center;padding:0 8px;gap:7px;font-size:8px;color:#555;font-weight:500}
.lang-flag{width:14px;height:9px;background:#2b3f8a}
.lang-select svg{margin-left:auto}
.main-nav a{position:absolute;top:55px;font-size:11.5px;color:var(--grey);text-decoration:none;letter-spacing:.2px;white-space:nowrap}
.main-nav a.active{color:var(--red)}
.feature{position:absolute;top:149px;width:161px;height:301px;border:1px solid var(--line);border-radius:3px;background:var(--white)}
.feature-art{position:absolute;left:16px;top:18px;width:128px;height:128px;border-radius:50%}
.feature-text{position:absolute;left:0;right:0;top:158px;font-family:'Arimo',sans-serif;font-size:11.2px;line-height:17.3px;color:var(--text);text-align:center;white-space:nowrap}
.art-globe{background:radial-gradient(circle at 40% 45%,#2fa7e8,#0a2a9e 60%,#020a3a)}
.art-analyst{background:radial-gradient(circle at 50% 60%,#1b2f6e,#1430b8 55%,#0a1450)}
.art-touch{background:radial-gradient(circle at 50% 50%,#d9a48b,#7fb7d8 55%,#2f6fa8)}
.art-hacker{background:radial-gradient(circle at 50% 50%,#ffffff,#9cc8f0 55%,#1f62c7)}
.video{position:absolute;left:733px;top:150px;width:431px;height:299px;border-radius:6px;overflow:hidden;box-shadow:0 1px 4px rgba(0,0,0,.3)}
.video-frame{position:absolute;inset:0;background:linear-gradient(160deg,#6f7f93 0%,#3d4a5b 45%,#1f2835 80%,#596779 100%)}
.video svg{position:absolute;inset:0}
.site-footer{position:absolute;left:0;top:510px;width:1200px;height:94px;background:var(--navy)}
.social{position:absolute;top:21px;left:535px;display:flex;gap:7px}
.social span{width:28px;height:28px;border:1.5px solid var(--white);border-radius:50%}
.footer-nav a{position:absolute;top:60px;font-size:9.6px;font-weight:700;color:var(--white);text-decoration:none;letter-spacing:.3px}
</style>
</head>
<body>
<header class="site-header">
  <div class="brand"><div class="brand-name">Keldro</div></div>
  <div class="lang">
    <span class="lang-label">SELECT LANGUAGE:</span>
    <div class="lang-select"><span class="lang-flag"></span>ENGLISH
      <svg width="10" height="7" viewBox="0 0 10 7"><path d="M1 1l4 4 4-4" fill="none" stroke="#666" stroke-width="1.5"/></svg>
    </div>
  </div>
  <nav class="main-nav">
    <a class="active" href="#" style="left:854px">COMPANY</a>
    <a href="#" style="left:950px">SERVICE</a>
    <a href="#" style="left:1038px">BLOG</a>
    <a href="#" style="left:1113px">CONTACT</a>
  </nav>
</header>

<section class="feature" style="left:33px">
  <div class="feature-art art-globe" role="img" aria-label="Digital globe with blue data overlay"></div>
  <p class="feature-text">Experts in cybersecurity.<br>Protect your digital asset.<br>We audit your company.<br>Excellent&nbsp; reputation<br>.</p>
</section>
<section class="feature" style="left:203px">
  <div class="feature-art art-analyst" role="img" aria-label="Security analyst seen from behind at a wall of monitors"></div>
  <p class="feature-text">Our team will detect all<br>your vulnerabilities. We<br>offer the best services. We<br>have extensive experience.<br>Results guarantee.</p>
</section>
<section class="feature" style="left:374px">
  <div class="feature-art art-touch" role="img" aria-label="Hand touching a digital fingerprint interface"></div>
  <p class="feature-text">We have the best<br>technologies and innovations<br>in cybersecurity. We manage<br>your problems in the fastest<br>and most economical way,<br>thanks to our remote service.</p>
</section>
<section class="feature" style="left:544px">
  <div class="feature-art art-hacker" role="img" aria-label="Silhouette of a hacker in front of a binary world map"></div>
  <p class="feature-text">We help you to know the<br>ways to protect your<br>company.<br>We offer you a personal<br>treatment and the best<br>advice with the necessary<br>services for you</p>
</section>

<div class="video">
  <div class="video-frame" role="img" aria-label="Video still of a padlock resting on a laptop keyboard"></div>
  <svg width="431" height="299" viewBox="0 0 431 299">
    <g fill="#3a4a6a" stroke="#c9d3e3" stroke-width="1.5">
      <circle cx="407" cy="42" r="10"/><circle cx="407" cy="72" r="10"/>
      <circle cx="407" cy="102" r="10"/><circle cx="407" cy="132" r="10"/>
    </g>
    <circle cx="219" cy="120" r="35" fill="rgba(255,255,255,.15)" stroke="rgba(255,255,255,.45)" stroke-width="3"/>
    <path d="M207 100v40l32-20z" fill="rgba(255,255,255,.4)"/>
    <rect x="7" y="263" width="417" height="29" rx="5" fill="#4a5a7e" stroke="#8f9dbb"/>
    <line x1="41" y1="264" x2="41" y2="291" stroke="#2a3552"/>
    <line x1="77" y1="264" x2="77" y2="291" stroke="#2a3552"/>
    <line x1="391" y1="264" x2="391" y2="291" stroke="#2a3552"/>
    <path d="M21 272v12l10-6z" fill="#fff"/>
    <path d="M52 275h3l4-3v12l-4-3h-3z" fill="#fff"/>
    <rect x="92" y="274" width="290" height="6" rx="3" fill="#111"/>
    <rect x="92" y="274" width="120" height="6" rx="3" fill="#e2101c"/>
    <circle cx="213" cy="277" r="6" fill="#8fa3c4" stroke="#fff"/>
    <rect x="402" y="271" width="12" height="12" fill="none" stroke="#fff" stroke-width="1.5"/>
  </svg>
</div>

<footer class="site-footer">
  <div class="social"><span></span><span></span><span></span></div>
  <nav class="footer-nav">
    <a href="#" style="left:473px">COMPANY</a>
    <a href="#" style="left:552px">SERVICE</a>
    <a href="#" style="left:623px">BLOG</a>
    <a href="#" style="left:683px">CONTACT</a>
  </nav>
</footer>
</body>
</html>
```